" Abrimos o escritório há poucos meses. Somos duas mulheres, a Sofia recém formada e a Berta formada há pouco mais de quatro anos. Estamos iniciando nossa carreira como advogadas esse ano, por enquanto, trabalhamos nós duas atuando nas mais diversas áreas do direito, sobretudo, cível, previdenciário e criminal. "

```html
<!DOCTYPE html>
<html lang="pt-BR">
<head>
<meta charset="UTF-8">
<title>Valente &amp; Moura Advocacia — Envelopes</title>
<link rel="stylesheet" href="https://fonts.googleapis.com/css2?family=Cormorant+Garamond:wght@400;500&family=Arimo:wght@400&display=swap">
<style>
  :root {
    --backdrop: #e9e5e0;
    --wine: #6a1a34;
    --wine-deep: #54102a;
    --wine-tint: #5a132d;
    --gold: #caa27c;
    --gold-light: #ecd2b2;
    --gold-dark: #9c7352;
    --paper-text: #f3e9ea;
  }
  * { margin: 0; padding: 0; box-sizing: border-box; }
  html, body {
    width: 1200px;
    height: 1200px;
    overflow: hidden;
    background: var(--backdrop);
  }
  .sheet {
    position: relative;
    width: 1200px;
    height: 1200px;
  }
  .envelope {
    position: absolute;
    top: 225px;
    width: 490px;
    height: 750px;
    background: var(--wine);
    box-shadow: 0 10px 26px rgba(0, 0, 0, 0.22);
    overflow: hidden;
  }
  .envelope--back { left: 85px; }
  .envelope--front { left: 625px; }

  .gold-band {
    position: absolute;
    left: 0;
    right: 0;
    bottom: 0;
    height: 9px;
    background: linear-gradient(90deg, var(--gold-dark), var(--gold-light) 35%, var(--gold) 60%, var(--gold-dark));
  }

  /* Back face */
  .back-mark {
    position: absolute;
    top: 58px;
    left: 0;
    right: 0;
    text-align: center;
    font-family: "Cormorant Garamond", serif;
    font-weight: 500;
    font-size: 15px;
    letter-spacing: 3px;
    color: var(--gold);
    text-transform: uppercase;
  }
  .back-decor {
    position: absolute;
    left: 22px;
    top: 150px;
    width: 400px;
    height: 400px;
    background: var(--wine-tint);
  }
  .contact {
    position: absolute;
    left: 0;
    right: 0;
    bottom: 34px;
    text-align: center;
    font-family: "Arimo", sans-serif;
    font-style: normal;
    font-size: 12px;
    line-height: 16px;
    color: var(--paper-text);
  }

  /* Front face */
  .flap {
    position: absolute;
    top: 0;
    left: 0;
    width: 490px;
    height: 190px;
  }
  .firm {
    position: absolute;
    top: 410px;
    left: 0;
    right: 0;
    text-align: center;
    color: var(--gold);
  }
  .firm__name {
    font-family: "Cormorant Garamond", serif;
    font-weight: 400;
    font-size: 26px;
    letter-spacing: 1px;
    text-transform: uppercase;
    display: inline-block;
    padding: 0 6px 4px;
    border-bottom: 1px solid var(--gold);
  }
  .firm__area {
    margin-top: 6px;
    font-family: "Cormorant Garamond", serif;
    font-weight: 400;
    font-size: 12px;
    letter-spacing: 7px;
    text-transform: uppercase;
  }
  .website {
    position: absolute;
    left: 0;
    right: 0;
    bottom: 30px;
    text-align: center;
    font-family: "Arimo", sans-serif;
    font-size: 12px;
    color: var(--paper-text);
  }
</style>
</head>
<body>
  <main class="sheet">
    <section class="envelope envelope--back" aria-label="Verso do envelope">
      <div class="back-mark">Valente &amp; Moura</div>
      <div class="back-decor" aria-hidden="true"></div>
      <address class="contact">
        contato@valentemoura.adv.br<br>
        (00) 0000-0000 &nbsp;&nbsp;&nbsp; (00) 00000-0000<br>
        Rua das Acácias nº120 - Jardim Sul - São Paulo - SP - 04500-010
      </address>
      <div class="gold-band"></div>
    </section>

    <section class="envelope envelope--front" aria-label="Frente do envelope">
      <svg class="flap" viewBox="0 0 490 190" aria-hidden="true">
        <path d="M0 0 H490 V40 L470 176 Q468 188 456 188 H34 Q22 188 20 176 L0 40 Z" fill="var(--wine-deep)"/>
      </svg>
      <div class="firm">
        <div class="firm__name">Valente &amp; Moura</div>
        <div class="firm__area">Advocacia</div>
      </div>
      <div class="website">www.valentemoura.adv.br</div>
      <div class="gold-band"></div>
    </section>
  </main>
</body>
</html>
```